Crestline Delivery Partners Business Card Redesign Project

CRESTLINE DELIVERY PARTNERS
Our company needs to have its business cards redesigned as the current design no longer reflects the business brand or attracts the type of clientele we are seeking.

MUST LOOK
★ Upmarket
★ Reflect Quality
★ Corporate feel
★ Professional
★ Innovative
★ Colourful

MUST PROMOTE
★ Market Leader
★ Knowledge
★ Expertise
★ Experience
★ Solutions
★ Advice

MUST FEEL
★ Classy
★ Elegant
★ Savvy
★ Edgy
★ Upbeat

WHAT WE DO
Crestline Delivery Partners provides project management and project controls consultancy services to companies in many industry sectors, within Australia and overseas. My company has developed a business brand through forging strong business relationships within industry. We provide innovative tools, concepts and solutions to management teams to assist them in better plan and managing there project portfolios.

SECTORS OF INDUSTRY WE SERVICE
★Oil & Gas
★Minerals & Metals
★Petrochemical
★Manufacturing
★Building & Construction
★Telecommunications
★Rail
★Civil

BUSINESS CARD DETAILS REQUIRED ON FRONT
Marcus Feldwick
Business Owner
Tel: 0498357162
Email: marcusfeldwick@crestlinedeliverypartners.com
Website: www.crestlinedeliverypartners.com.au

BUSINESS CARD DETAILS REQUIRED ON BACK
Providing | Knowledge | Expertise | Experience

ATTACHMENTS
Business Logo

Target Market(s)

Oil & Gas I Mining & Resources I Industry in General
Upmarket Clientele
Corporate World

Industry/Entity Type

Industry

Requirements
Must have
• Must be creative and a unique design
The business card must have information on the front and back

```html
<!DOCTYPE html>
<html lang="en">
<head>
<meta charset="utf-8">
<title>Crestline Delivery Partners – Business Cards</title>
<link rel="stylesheet" href="https://fonts.googleapis.com/css2?family=Open+Sans:wght@300;400;600;700&display=swap">
<style>
  :root {
    --stage: #3a3230;
    --card-white: #ffffff;
    --brand-red: #e21f26;
    --ink: #231f20;
    --grey-text: #555555;
    --rule: #8a8a8a;
    --label: #ffffff;
  }
  * { box-sizing: border-box; margin: 0; padding: 0; }
  html, body { width: 1200px; height: 913px; overflow: hidden; }
  body {
    background: var(--stage);
    font-family: "Open Sans", Arial, sans-serif;
    position: relative;
  }
  .card {
    position: absolute;
    width: 460px;
    height: 262px;
    background: var(--card-white);
    box-shadow: 0 4px 10px rgba(0,0,0,.35);
  }
  .card--front  { left: 108px; top: 145px; }
  .card--back-1 { left: 603px; top: 139px; background: var(--brand-red); }
  .card--back-2 { left: 110px; top: 447px; }
  .card--back-3 { left: 605px; top: 436px; }

  .view-label {
    position: absolute;
    color: var(--label);
    font-size: 32px;
    font-weight: 400;
  }
  .view-label--1 { left: 944px; top: 88px; }
  .view-label--2 { left: 127px; top: 732px; }
  .view-label--3 { left: 979px; top: 728px; }

  /* front */
  .brand {
    position: absolute;
    display: flex;
    align-items: center;
    gap: 10px;
  }
  .brand__dot {
    width: 16px; height: 16px;
    border-radius: 50%;
    background: var(--brand-red);
    flex: none;
  }
  .brand__name {
    font-weight: 600;
    color: var(--ink);
    letter-spacing: .02em;
  }
  .card--front .brand { left: 22px; top: 54px; }
  .card--front .brand__name { font-size: 19px; }
  .tagline {
    position: absolute;
    left: 48px; top: 84px;
    font-size: 7.5px;
    color: var(--ink);
  }
  .holder {
    position: absolute;
    left: 134px; top: 148px;
    display: flex; align-items: baseline; gap: 8px;
  }
  .holder__name {
    font-size: 17px; font-weight: 700;
    color: var(--brand-red);
    text-transform: uppercase;
  }
  .holder__role { font-size: 11px; color: var(--ink); }
  .holder-rule {
    position: absolute;
    left: 134px; top: 175px;
    width: 244px; height: 1px;
    background: var(--rule);
  }
  .contacts {
    position: absolute;
    left: 134px; top: 192px;
    list-style: none;
  }
  .contacts li {
    display: flex; align-items: center; gap: 7px;
    font-size: 11px; color: var(--ink);
    height: 18px;
  }
  .contacts svg { width: 12px; height: 12px; fill: var(--brand-red); flex: none; }

  /* backs */
  .values {
    position: absolute;
    list-style: none;
    text-align: center;
    font-weight: 300;
    font-size: 19px;
    line-height: 32px;
    text-transform: uppercase;
  }
  .card--back-1 .values { left: 222px; top: 68px; color: var(--card-white); }
  .card--back-3 .values { left: 222px; top: 62px; color: var(--grey-text); }

  .card--back-1 .brand { left: 62px; top: 120px; }
  .card--back-1 .brand__dot { background: var(--card-white); }
  .card--back-1 .brand__name { color: var(--card-white); font-size: 15px; width: 130px; line-height: 1.3; }
  .card--back-3 .brand { left: 62px; top: 114px; }
  .card--back-3 .brand__name { font-size: 15px; width: 130px; line-height: 1.3; }
  .card--back-2 .brand { left: 0; right: 0; top: 98px; justify-content: center; }
  .card--back-2 .brand__name { font-size: 19px; }

  .value-strip {
    position: absolute;
    left: 0; right: 0; top: 218px;
    display: flex; justify-content: center; gap: 6px;
    list-style: none;
    font-size: 13.5px; font-weight: 400;
    color: var(--grey-text);
    text-transform: uppercase;
  }
  .value-strip li { display: flex; align-items: center; gap: 5px; }
  .value-strip li::before {
    content: ""; width: 8px; height: 8px; border-radius: 50%;
    background: linear-gradient(90deg, var(--brand-red) 50%, var(--ink) 50%);
  }
</style>
</head>
<body>
  <span class="view-label view-label--1">Back 1</span>
  <span class="view-label view-label--2">Back 2</span>
  <span class="view-label view-label--3">Back 3</span>

  <section class="card card--front" aria-label="Card front">
    <div class="brand"><span class="brand__dot"></span><span class="brand__name">Crestline Delivery Partners</span></div>
    <p class="tagline">Providing Effective Project Controls and Management Solutions</p>
    <div class="holder"><span class="holder__name">Marcus Feldwick,</span><span class="holder__role">Business Owner</span></div>
    <div class="holder-rule"></div>
    <ul class="contacts">
      <li><svg viewBox="0 0 24 24"><path d="M6.6 10.8a15.1 15.1 0 0 0 6.6 6.6l2.2-2.2a1 1 0 0 1 1-.25 11.4 11.4 0 0 0 3.6.57 1 1 0 0 1 1 1V20a1 1 0 0 1-1 1A17 17 0 0 1 3 4a1 1 0 0 1 1-1h3.5a1 1 0 0 1 1 1c0 1.25.2 2.45.57 3.57a1 1 0 0 1-.25 1z"/></svg>0498357162</li>
      <li><svg viewBox="0 0 24 24"><path d="M2 5h20v14H2zM4 7v.5l8 5 8-5V7l-8 5z"/></svg>marcusfeldwick@crestlinedeliverypartners.com</li>
      <li><svg viewBox="0 0 24 24"><path d="M12 2a10 10 0 1 0 0 20 10 10 0 0 0 0-20zm6.9 6h-3a15 15 0 0 0-1.3-3.9A8 8 0 0 1 18.9 8zM12 4c.8 1.2 1.5 2.5 1.9 4h-3.8c.4-1.5 1.1-2.8 1.9-4zM4.3 14a8 8 0 0 1 0-4h3.4a16 16 0 0 0 0 4zm.8 2h3a15 15 0 0 0 1.3 3.9A8 8 0 0 1 5.1 16zm3-8h-3a8 8 0 0 1 4.3-3.9A15 15 0 0 0 8.1 8zM12 20c-.8-1.2-1.5-2.5-1.9-4h3.8c-.4 1.5-1.1 2.8-1.9 4zm2.3-6H9.7a14 14 0 0 1 0-4h4.6a14 14 0 0 1 0 4zm.3 5.9a15 15 0 0 0 1.3-3.9h3a8 8 0 0 1-4.3 3.9zm1.7-5.9a16 16 0 0 0 0-4h3.4a8 8 0 0 1 0 4z"/></svg>www.crestlinedeliverypartners.com.au</li>
    </ul>
  </section>

  <section class="card card--back-1" aria-label="Card back, red">
    <div class="brand"><span class="brand__dot"></span><span class="brand__name">Crestline Delivery Partners</span></div>
    <ul class="values"><li>Providing</li><li>Knowledge</li><li>Expertise</li><li>Experience</li></ul>
  </section>

  <section class="card card--back-2" aria-label="Card back, centred">
    <div class="brand"><span class="brand__dot"></span><span class="brand__name">Crestline Delivery Partners</span></div>
    <ul class="value-strip"><li>Providing</li><li>Knowledge</li><li>Expertise</li><li>Experience</li></ul>
  </section>

  <section class="card card--back-3" aria-label="Card back, white">
    <div class="brand"><span class="brand__dot"></span><span class="brand__name">Crestline Delivery Partners</span></div>
    <ul class="values"><li>Providing</li><li>Knowledge</li><li>Expertise</li><li>Experience</li></ul>
  </section>
</body>
</html>
```